Business Card Design

Im a makeup artist looking for some business cards but need help with creating it.

Industry/Entity Type

Business

Contact Information for Business Card

Mara Penhallow
email mara.penhallow3@brindlemail.net
phone number 0284630928

Requirements
Must have
• i have a logo that i think would work and that i have as my logo on Lumigram. i would like maybe something at the bottom on the card saying like me on Lumigram or something like that.
Nice to have
• Nice writing, my logo as the main item. So its what people are drawn too. to have a glossy card.

```html
<!DOCTYPE html>
<html lang="en">
<head>
<meta charset="utf-8">
<title>Mara Penhallow Makeup – Business Card</title>
<link rel="stylesheet" href="https://fonts.googleapis.com/css2?family=Libre+Baskerville:wght@400;700&display=swap">
<style>
  :root {
    --backdrop: #ececec;
    --card-white: #ffffff;
    --ink: #111111;
    --ink-soft: #222222;
    --lavender: #d8a9dc;
    --orchid: #c55bb3;
    --magenta: #dc3589;
    --rose-red: #ea2a5a;
    --plum: #7c2a4d;
    --icon-fill: #f5d3df;
    --night: #000000;
  }

  * { box-sizing: border-box; margin: 0; padding: 0; }

  html, body {
    width: 1200px;
    height: 533px;
    overflow: hidden;
    background: var(--backdrop);
  }

  .canvas {
    position: relative;
    width: 1200px;
    height: 533px;
    font-family: "Libre Baskerville", "Times New Roman", serif;
    color: var(--ink);
  }

  .card {
    position: absolute;
    top: 99px;
    height: 317px;
    overflow: hidden;
    box-shadow: 3px 4px 6px rgba(0, 0, 0, 0.35);
  }

  /* ---------- Front card ---------- */
  .card--front {
    left: 67px;
    width: 548px;
    background: var(--card-white);
  }

  .front__panel {
    position: absolute;
    left: 0; top: 0;
    width: 177px; height: 100%;
    background:
      radial-gradient(ellipse 60% 30% at 55% 18%, rgba(160, 70, 150, 0.45), transparent 70%),
      radial-gradient(ellipse 50% 25% at 40% 78%, rgba(140, 60, 130, 0.35), transparent 70%),
      linear-gradient(180deg, var(--lavender) 0%, var(--orchid) 30%, var(--magenta) 62%, var(--rose-red) 100%);
  }

  .front__flourish-top {
    position: absolute;
    right: 0; top: 0;
    width: 220px; height: 160px;
    background:
      radial-gradient(ellipse 45% 55% at 70% 35%, rgba(214, 86, 150, 0.5), transparent 72%),
      radial-gradient(ellipse 40% 40% at 40% 75%, rgba(243, 182, 211, 0.6), transparent 70%);
  }

  .front__flourish-bottom {
    position: absolute;
    right: 0; bottom: 0;
    width: 180px; height: 140px;
    background:
      radial-gradient(ellipse 55% 55% at 65% 65%, rgba(150, 70, 95, 0.5), transparent 72%),
      radial-gradient(ellipse 40% 40% at 85% 25%, rgba(214, 110, 150, 0.45), transparent 70%);
  }

  .front__rule {
    position: absolute;
    left: 196px;
    height: 12px;
    background: linear-gradient(90deg, rgba(200, 80, 130, 0.55), rgba(243, 182, 211, 0.35) 70%, transparent);
    border-radius: 6px;
  }
  .front__rule--above { top: 22px; width: 140px; }
  .front__rule--below { top: 128px; width: 190px; }

  .brand-block {
    position: absolute;
    background: var(--card-white);
    display: flex;
    align-items: center;
    justify-content: center;
    text-align: center;
  }

  .brand__name {
    font-weight: 400;
    color: var(--ink);
    line-height: 1.25;
  }

  .brand-block--front {
    left: 0; top: 114px;
    width: 170px; height: 62px;
    border-radius: 0 12px 12px 0;
  }
  .brand-block--front .brand__name { font-size: 17px; }

  .front__name {
    position: absolute;
    left: 198px; top: 58px;
    font-size: 25px;
    font-weight: 400;
    letter-spacing: 1.5px;
    text-transform: uppercase;
    color: var(--ink-soft);
    white-space: nowrap;
  }

  .contact-row {
    position: absolute;
    left: 192px;
    display: flex;
    align-items: center;
  }
  .contact-row--phone { top: 183px; }
  .contact-row--email { top: 236px; }

  .contact-icon {
    width: 34px; height: 34px;
    flex: none;
  }

  .contact__phone {
    margin-left: 38px;
    font-size: 24px;
    font-weight: 700;
    letter-spacing: 0.5px;
  }
  .contact__email {
    margin-left: 22px;
    font-size: 15px;
    font-weight: 400;
    white-space: nowrap;
  }

  .front__social {
    position: absolute;
    left: 248px; top: 285px;
    font-size: 12px;
    font-weight: 400;
    color: var(--ink-soft);
    letter-spacing: 0.5px;
  }

  /* ---------- Back card ---------- */
  .card--back {
    left: 622px;
    width: 516px;
    background: var(--night);
  }

  .back__smoke {
    position: absolute;
    inset: 0;
    background:
      radial-gradient(ellipse 22% 30% at 12% 28%, rgba(138, 122, 128, 0.75), transparent 72%),
      radial-gradient(ellipse 20% 20% at 30% 12%, rgba(150, 135, 140, 0.55), transparent 72%),
      radial-gradient(ellipse 18% 22% at 55% 8%, rgba(120, 100, 108, 0.45), transparent 72%),
      radial-gradient(ellipse 20% 20% at 82% 10%, rgba(130, 110, 118, 0.5), transparent 72%),
      radial-gradient(ellipse 26% 30% at 14% 85%, rgba(142, 52, 69, 0.6), transparent 72%),
      radial-gradient(ellipse 22% 36% at 86% 60%, rgba(160, 70, 85, 0.65), transparent 72%),
      radial-gradient(ellipse 18% 20% at 60% 92%, rgba(120, 50, 65, 0.45), transparent 72%);
  }

  .brand-block--back {
    left: 168px; top: 70px;
    width: 162px; height: 172px;
    padding: 0 10px;
  }
  .brand-block--back .brand__name { font-size: 21px; }
</style>
</head>
<body>
<main class="canvas">

  <section class="card card--front" aria-label="Business card front">
    <div class="front__panel" role="img" aria-label="Pink and lavender panel with swirling floral ornaments"></div>
    <div class="front__flourish-top" role="img" aria-label="Pink floral flourish ornament"></div>
    <div class="front__flourish-bottom" role="img" aria-label="Rose floral swirl ornament"></div>
    <div class="front__rule front__rule--above" role="img" aria-label="Decorative scroll ornament"></div>
    <div class="front__rule front__rule--below" role="img" aria-label="Decorative scroll ornament"></div>

    <div class="brand-block brand-block--front">
      <span class="brand__name">Mara Penhallow Makeup</span>
    </div>

    <h1 class="front__name">Mara Penhallow</h1>

    <div class="contact-row contact-row--phone">
      <svg class="contact-icon" viewBox="0 0 36 36" aria-hidden="true">
        <circle cx="18" cy="18" r="16.5" fill="var(--icon-fill)" stroke="var(--plum)" stroke-width="2"/>
        <path d="M12.5 10.5c1-1 2.2-.8 2.8.2l1.6 2.7c.5.8.3 1.7-.4 2.2l-1 .8c.8 2 2.3 3.6 4.2 4.6l.9-1c.6-.6 1.5-.7 2.2-.2l2.6 1.7c.9.6 1 1.9.1 2.7l-1.2 1.1c-1 .9-2.5 1.1-3.8.5-4.2-1.9-7.4-5.3-9-9.6-.5-1.3-.2-2.7.8-3.6z" fill="var(--plum)"/>
      </svg>
      <span class="contact__phone">0284630928</span>
    </div>

    <div class="contact-row contact-row--email">
      <svg class="contact-icon" viewBox="0 0 36 36" aria-hidden="true">
        <circle cx="18" cy="18" r="16.5" fill="var(--icon-fill)" stroke="var(--plum)" stroke-width="2"/>
        <rect x="9" y="12" width="18" height="12" rx="1" fill="#fff" stroke="var(--plum)" stroke-width="1.6"/>
        <path d="M9.5 12.8 18 19l8.5-6.2" fill="none" stroke="var(--plum)" stroke-width="1.6"/>
      </svg>
      <span class="contact__email">mara.penhallow3@brindlemail.net</span>
    </div>

    <p class="front__social">Like me on Lumigram</p>
  </section>

  <section class="card card--back" aria-label="Business card back">
    <div class="back__smoke" role="img" aria-label="Smoky grey and wine floral ornaments on black"></div>
    <div class="brand-block brand-block--back">
      <span class="brand__name">Mara Penhallow Makeup</span>
    </div>
  </section>

</main>
</body>
</html>
```